I need this design by August 8th or 9th!
Looking for a classy, but FUn door hangers for a community outreach "Maple Lantern Funfair." While we are a faith-based organization, we do NOT want this to look religious. I put the DW square blue so you would have a color reference. With grey and orange as an accent color.
Event: Maple Lantern Funfair!
Location: Calloway Pines Estate neighborhood pavilion by the red silo.
Date: Friday, August 17th
Time: 5:30 p.m. to 8:30 p.m.
Free food, while supplies last!
Yummy desserts,
Bounce house,
Raffle,
Games and activities.

Target Market(s)

Families in the neighborhood

Colors
acd136
959595
fbee3d

Requirements
Must have
• Door hanger,

```html
<!DOCTYPE html>
<html lang="en">
<head>
<meta charset="utf-8">
<title>Maple Lantern Funfair – Door Hanger</title>
<link href="https://fonts.googleapis.com/css2?family=Oswald:wght@600;700&family=Arimo:wght@400;700&family=Questrial&family=Satisfy&display=swap" rel="stylesheet">
<style>
  :root {
    --page: #ebe7e1;
    --ink: #000000;
    --orange: #e8870e;
    --grey-light: #d9d9d9;
    --white: #ffffff;
    --steel-blue: #4f7b9b;
    --sky-top: #8a8468;
    --sky-mid: #b59a62;
    --sky-glow: #e0962c;
    --sky-sun: #f6c24a;
  }
  * { margin: 0; padding: 0; box-sizing: border-box; }
  html, body { width: 1200px; height: 1200px; overflow: hidden; background: var(--page); }
  .canvas { position: relative; width: 1200px; height: 1200px; }

  .door-hanger {
    position: absolute; left: 360px; top: 30px;
    width: 480px; height: 1140px;
    background: var(--ink); color: var(--white);
    overflow: hidden;
  }
  .hero-photo {
    position: absolute; left: 0; top: 0; width: 480px; height: 527px;
    background:
      radial-gradient(ellipse 120px 60px at 265px 510px, var(--sky-sun) 0%, rgba(246,194,74,0) 100%),
      linear-gradient(180deg, var(--sky-top) 0%, #9c8f6a 40%, var(--sky-mid) 60%, var(--sky-glow) 88%, #c8731a 100%);
  }
  .die-cut { position: absolute; left: 0; top: 0; }

  .event-title {
    position: absolute; left: 0; top: 545px; width: 100%;
    text-align: center;
    font-family: "Oswald", "Arial Narrow", sans-serif; font-weight: 700;
    font-size: 46px; line-height: 56px; text-transform: uppercase;
  }
  .event-title .line-accent { color: var(--orange); display: block; }
  .event-title .line-main { color: var(--grey-light); display: block; }

  .details { font-family: "Arimo", Arial, sans-serif; }
  .detail-row { position: absolute; left: 0; width: 100%; text-align: center; font-size: 24px; }
  .detail-row .label { color: var(--orange); font-weight: 700; }
  .row-date { top: 684px; }
  .row-date .value { font-weight: 700; }
  .row-time { top: 730px; }
  .row-location { top: 780px; left: 62px; width: 400px; display: flex; text-align: left; font-size: 21px; }
  .row-location .label { margin-right: 6px; line-height: 26px; }
  .row-location .value { text-align: center; line-height: 26px; }

  .free-food {
    position: absolute; left: 62px; top: 868px;
    font-family: "Oswald", "Arial Narrow", sans-serif; font-weight: 700;
    font-size: 62px; line-height: 56px; text-transform: uppercase;
  }
  .free-food .word-free { color: var(--orange); display: block; }
  .free-food .word-food { color: var(--steel-blue); display: block; }
  .free-food .note {
    display: block; margin-top: 6px; text-transform: none;
    font-family: "Arimo", Arial, sans-serif; font-weight: 400; font-size: 16px; line-height: 20px;
    color: var(--white); letter-spacing: -0.5px;
  }

  .perks { position: absolute; left: 215px; top: 880px; list-style: none;
    font-family: "Questrial", "Century Gothic", sans-serif; font-size: 22px; }
  .perks li { display: flex; align-items: center; height: 33px; letter-spacing: 0.5px; }
  .perks svg { margin-right: 10px; flex: none; }

  .hashtag {
    position: absolute; left: 0; top: 1050px; width: 100%; text-align: center;
    font-family: "Satisfy", cursive; font-size: 44px; color: var(--white);
  }
</style>
</head>
<body>
<div class="canvas">
  <article class="door-hanger">
    <div class="hero-photo" role="img" aria-label="Photo of a row of people jumping in silhouette against a golden sunset"></div>
    <svg class="die-cut" width="480" height="527" viewBox="0 0 480 527" aria-hidden="true">
      <polygon points="112,0 140,0 222,112 200,124" fill="var(--page)"/>
      <circle cx="239" cy="187" r="98" fill="var(--page)"/>
    </svg>

    <h1 class="event-title">
      <span class="line-accent">Maple Lantern</span>
      <span class="line-main">Funfair</span>
    </h1>

    <div class="details">
      <p class="detail-row row-date"><span class="label">DATE:</span> <span class="value">Friday, August 17th</span></p>
      <p class="detail-row row-time"><span class="label">Time:</span> <span class="value">5:30 p.m. to 8:30 p.m.</span></p>
      <p class="detail-row row-location"><span class="label">LOCATION:</span>
        <span class="value">Calloway Pines Estate<br>neighborhood pavilion<br>by the red silo.</span></p>
    </div>

    <p class="free-food">
      <span class="word-free">Free</span>
      <span class="word-food">Food</span>
      <span class="note">while supplies last!</span>
    </p>

    <ul class="perks">
      <li><svg width="14" height="14" viewBox="0 0 14 14"><circle cx="7" cy="7" r="7" fill="var(--orange)"/><path d="M3.8 7.2l2.2 2.1 4.2-4.4" stroke="var(--ink)" stroke-width="1.8" fill="none"/></svg>Yummy desserts</li>
      <li><svg width="14" height="14" viewBox="0 0 14 14"><circle cx="7" cy="7" r="7" fill="var(--orange)"/><path d="M3.8 7.2l2.2 2.1 4.2-4.4" stroke="var(--ink)" stroke-width="1.8" fill="none"/></svg>Bouncy house</li>
      <li><svg width="14" height="14" viewBox="0 0 14 14"><circle cx="7" cy="7" r="7" fill="var(--orange)"/><path d="M3.8 7.2l2.2 2.1 4.2-4.4" stroke="var(--ink)" stroke-width="1.8" fill="none"/></svg>Raffle</li>
      <li><svg width="14" height="14" viewBox="0 0 14 14"><circle cx="7" cy="7" r="7" fill="var(--orange)"/><path d="M3.8 7.2l2.2 2.1 4.2-4.4" stroke="var(--ink)" stroke-width="1.8" fill="none"/></svg>Games &amp; activities</li>
    </ul>

    <p class="hashtag">#ForMapleton</p>
  </article>
</div>
</body>
</html>
```